I need three graphics made that will go on walls in a basketball lockerroom

I need three graphics made that will go on a basketball lockerroom wall. Here are the specifics.
Graphic 1 (Size 115" wide by 52" tall, min 150 DPI)
This should be something that displays the acronym for MARLOW. The main background color should be the teal color attached. Use logos and the other approved colors as needed.
Standards
Intensity
Effort
Grit
Energy
Love
Graphic 2 (Size 88" wide by 52" tall, min 150 DPI)
This one should be on the Navy Blue background color attached
and impactful way say Attitude and Effort
Graphic 3 (Size 100" wide by 18" tall, min 150 DPI)
This goes along the top of the way and needs to say
(MHS logo) Foxes Lead the Way (Fox logo) Marlow Basketball (MHS logo)
All three of these need to feel like they are of the same style. For Graphic #2 I thought something maybe like the attached basketball except use the M Fox in the middle and say attitude and effort using the colors .. but I'm open to other ideas

```html
<!DOCTYPE html>
<html lang="en">
<head>
<meta charset="utf-8">
<title>Marlow Basketball Locker Room Graphics</title>
<link rel="stylesheet" href="https://fonts.googleapis.com/css2?family=Alfa+Slab+One&family=Exo+2:ital,wght@1,800&family=Open+Sans:wght@400&family=Teko:wght@500;600&display=swap">
<style>
  :root {
    --teal: #0a7a82;
    --teal-bright: #13878d;
    --navy: #1b365d;
    --silver: #a7a9ac;
    --slate: #5e6b7d;
    --white: #ffffff;
    --ink: #000000;
  }
  * { box-sizing: border-box; }
  html, body {
    margin: 0;
    width: 1200px;
    height: 720px;
    overflow: hidden;
    background: var(--white);
  }
  .sheet { position: relative; width: 1200px; height: 720px; }
  .graphic-number {
    position: absolute;
    margin: 0;
    font-family: "Open Sans", sans-serif;
    font-weight: 400;
    font-size: 54px;
    line-height: 1;
    color: var(--ink);
  }
  .graphic-number--one { left: 72px; top: 20px; }
  .graphic-number--two { left: 773px; top: 20px; }
  .graphic-number--three { left: 585px; top: 417px; }
  .graphic { position: absolute; display: block; }
  .graphic--values { left: 23px; top: 81px; width: 708px; height: 321px; }
  .graphic--attitude { left: 758px; top: 109px; width: 416px; height: 246px; }
  .graphic--banner { left: 27px; top: 474px; width: 1145px; height: 206px; }

  .acronym-letter {
    font-family: "Alfa Slab One", serif;
    font-size: 92px;
    fill: var(--silver);
    stroke: var(--navy);
    stroke-width: 9px;
    paint-order: stroke;
    stroke-linejoin: round;
  }
  .value-word {
    font-family: "Exo 2", sans-serif;
    font-style: italic;
    font-weight: 800;
    font-size: 11.5px;
    fill: var(--white);
  }
  .value-star { fill: none; stroke: var(--navy); stroke-width: 1.4px; }
  .team-initials {
    font-family: "Teko", sans-serif;
    font-weight: 600;
    fill: var(--silver);
  }
  .motto-word {
    font-family: "Teko", sans-serif;
    font-weight: 600;
    font-size: 29px;
    letter-spacing: 0.5px;
    fill: var(--silver);
  }
  .banner-phrase {
    font-family: "Teko", sans-serif;
    font-weight: 600;
    font-size: 64px;
  }
  .fill-teal { fill: var(--teal-bright); }
  .fill-silver { fill: var(--silver); }
</style>
</head>
<body>
<main class="sheet">

  <h2 class="graphic-number graphic-number--one">01</h2>
  <svg class="graphic graphic--values" viewBox="0 0 708 321" role="img" aria-label="Marlow values wall graphic">
    <rect width="708" height="321" fill="var(--teal)"/>
    <g class="corner-shards corner-shards--left">
      <polygon points="0,170 62,225 0,185" fill="var(--silver)"/>
      <polygon points="0,205 105,290 0,225" fill="var(--silver)"/>
      <polygon points="0,232 70,270 0,250" fill="var(--silver)"/>
      <polygon points="0,240 88,321 52,321 0,275" fill="var(--navy)"/>
      <polygon points="0,275 75,305 0,290" fill="var(--navy)"/>
      <polygon points="10,250 110,321 95,321 0,262" fill="var(--navy)"/>
    </g>
    <g class="corner-shards corner-shards--right">
      <polygon points="708,165 648,218 708,180" fill="var(--silver)"/>
      <polygon points="708,195 605,283 708,215" fill="var(--silver)"/>
      <polygon points="708,228 660,262 708,245" fill="var(--silver)"/>
      <polygon points="708,238 615,321 650,321 708,272" fill="var(--navy)"/>
      <polygon points="708,262 640,300 708,285" fill="var(--navy)"/>
    </g>

    <g class="acronym" transform="skewX(-8) translate(14 0)">
      <text class="acronym-letter" x="40" y="127" textLength="76" lengthAdjust="spacingAndGlyphs">M</text>
      <text class="acronym-letter" x="146" y="127" textLength="76" lengthAdjust="spacingAndGlyphs">A</text>
      <text class="acronym-letter" x="250" y="127" textLength="76" lengthAdjust="spacingAndGlyphs">R</text>
      <text class="acronym-letter" x="367" y="127" textLength="76" lengthAdjust="spacingAndGlyphs">L</text>
      <text class="acronym-letter" x="486" y="127" textLength="76" lengthAdjust="spacingAndGlyphs">O</text>
      <text class="acronym-letter" x="597" y="127" textLength="76" lengthAdjust="spacingAndGlyphs">W</text>
    </g>

    <g class="values-row" text-anchor="middle">
      <text class="value-word" x="77" y="164">STANDARDS</text>
      <text class="value-word" x="182" y="164">INTENSITY</text>
      <text class="value-word" x="286" y="164">EFFORT</text>
      <text class="value-word" x="402" y="164">GRIT</text>
      <text class="value-word" x="521" y="164">ENERGY</text>
      <text class="value-word" x="632" y="164">LOVE</text>
    </g>
    <g class="value-underlines" fill="var(--navy)">
      <polygon points="53,178 102,178 100,181 51,181"/>
      <polygon points="158,178 207,178 205,181 156,181"/>
      <polygon points="262,178 311,178 309,181 260,181"/>
      <polygon points="378,178 427,178 425,181 376,181"/>
      <polygon points="497,178 546,178 544,181 495,181"/>
      <polygon points="608,178 657,178 655,181 606,181"/>
    </g>
    <g class="value-stars">
      <polygon class="value-star" transform="translate(77 197)" points="0,-7 1.6,-2.2 6.7,-2.2 2.6,0.8 4.1,5.7 0,2.7 -4.1,5.7 -2.6,0.8 -6.7,-2.2 -1.6,-2.2"/>
      <polygon class="value-star" transform="translate(182 197)" points="0,-7 1.6,-2.2 6.7,-2.2 2.6,0.8 4.1,5.7 0,2.7 -4.1,5.7 -2.6,0.8 -6.7,-2.2 -1.6,-2.2"/>
      <polygon class="value-star" transform="translate(286 197)" points="0,-7 1.6,-2.2 6.7,-2.2 2.6,0.8 4.1,5.7 0,2.7 -4.1,5.7 -2.6,0.8 -6.7,-2.2 -1.6,-2.2"/>
      <polygon class="value-star" transform="translate(402 197)" points="0,-7 1.6,-2.2 6.7,-2.2 2.6,0.8 4.1,5.7 0,2.7 -4.1,5.7 -2.6,0.8 -6.7,-2.2 -1.6,-2.2"/>
      <polygon class="value-star" transform="translate(521 197)" points="0,-7 1.6,-2.2 6.7,-2.2 2.6,0.8 4.1,5.7 0,2.7 -4.1,5.7 -2.6,0.8 -6.7,-2.2 -1.6,-2.2"/>
      <polygon class="value-star" transform="translate(632 197)" points="0,-7 1.6,-2.2 6.7,-2.2 2.6,0.8 4.1,5.7 0,2.7 -4.1,5.7 -2.6,0.8 -6.7,-2.2 -1.6,-2.2"/>
    </g>
    <g class="value-dividers" stroke="var(--white)" stroke-width="1.5">
      <line x1="133" y1="150" x2="133" y2="204"/>
      <line x1="226" y1="150" x2="226" y2="204"/>
      <line x1="340" y1="150" x2="340" y2="204"/>
      <line x1="457" y1="150" x2="457" y2="204"/>
      <line x1="576" y1="150" x2="576" y2="204"/>
    </g>

    <g class="center-rule">
      <polygon points="104,252 289,248 289,256" fill="var(--navy)" stroke="var(--silver)" stroke-width="0.8"/>
      <polygon points="420,248 605,252 420,256" fill="var(--navy)" stroke="var(--silver)" stroke-width="0.8"/>
    </g>
    <text class="team-initials" x="354" y="272" font-size="54" text-anchor="middle">MHS</text>
  </svg>

  <h2 class="graphic-number graphic-number--two">02</h2>
  <svg class="graphic graphic--attitude" viewBox="0 0 416 246" role="img" aria-label="Attitude and effort wall graphic">
    <rect width="416" height="246" fill="var(--navy)"/>
    <g class="speed-rules">
      <polygon points="4,86 134,83 134,87" fill="var(--silver)"/>
      <polygon points="20,90 134,88 134,91" fill="var(--teal-bright)"/>
      <polygon points="4,155 134,152 134,156" fill="var(--silver)"/>
      <polygon points="20,159 134,157 134,160" fill="var(--teal-bright)"/>
      <polygon points="282,83 412,86 282,87" fill="var(--silver)"/>
      <polygon points="282,88 396,90 282,91" fill="var(--teal-bright)"/>
      <polygon points="282,152 412,155 282,156" fill="var(--silver)"/>
      <polygon points="282,157 396,159 282,160" fill="var(--teal-bright)"/>
    </g>
    <circle cx="208" cy="123" r="70" fill="var(--navy)" stroke="var(--silver)" stroke-width="3"/>
    <text class="team-initials" x="208" y="135" font-size="36" text-anchor="middle">M FOX</text>
    <text class="motto-word" x="68" y="136" text-anchor="middle">ATTITUDE</text>
    <text class="motto-word" x="346" y="136" text-anchor="middle">EFFORT</text>
  </svg>

  <h2 class="graphic-number graphic-number--three">03</h2>
  <svg class="graphic graphic--banner" viewBox="0 0 1145 206" role="img" aria-label="Foxes Lead the Way banner">
    <rect width="1145" height="206" fill="var(--navy)"/>
    <rect y="32" width="1145" height="4" fill="var(--white)"/>
    <rect y="171" width="1145" height="4" fill="var(--white)"/>
    <text class="team-initials" x="94" y="127" font-size="74" text-anchor="middle">MHS</text>
    <text class="banner-phrase" x="184" y="128" textLength="324" lengthAdjust="spacingAndGlyphs"><tspan class="fill-teal">FOXES </tspan><tspan class="fill-silver">LEAD </tspan><tspan class="fill-teal">THE </tspan><tspan class="fill-silver">WAY</tspan></text>
    <text class="team-initials" x="579" y="122" font-size="40" text-anchor="middle">M FOX</text>
    <text class="banner-phrase" x="650" y="128" textLength="306" lengthAdjust="spacingAndGlyphs"><tspan class="fill-silver">MARLOW </tspan><tspan class="fill-teal">BASKETBALL</tspan></text>
    <text class="team-initials" x="1050" y="127" font-size="74" text-anchor="middle">MHS</text>
  </svg>

</main>
</body>
</html>
```